New Book Cover Design Project

Book Cover with this title and sub title
Lessons Taught by the Old Orchard Hives
A pocket guide to careful spending and caring for nature.
Walter P. Kolb Ph. D.
Ruth P. Kolb
Picture below would be on the entire front cover. Words somehow incorporated for easy reading.

```html
<!DOCTYPE html>
<html lang="en">
<head>
<meta charset="utf-8">
<title>Lessons Taught by the Old Orchard Hives — Book Cover</title>
<link rel="stylesheet" href="https://fonts.googleapis.com/css2?family=Cinzel:wght@400;700&family=Oswald:wght@500&display=swap">
<style>
  :root {
    --backdrop: #7d8797;
    --petal-light: #f7cf1c;
    --petal-mid: #eab20f;
    --petal-deep: #c98d06;
    --disc-dark: #5a3a05;
    --disc-amber: #a86a04;
    --ink-white: #ffffff;
    --ink-gold: #e2b21a;
    --spine-shade: rgba(0, 0, 0, 0.18);
  }
  * { margin: 0; padding: 0; box-sizing: border-box; }
  html, body {
    width: 1200px;
    height: 1122px;
    overflow: hidden;
    background: var(--backdrop);
  }
  .canvas {
    position: relative;
    width: 1200px;
    height: 1122px;
    display: flex;
    align-items: center;
    justify-content: center;
  }
  .book-cover {
    position: relative;
    width: 720px;
    height: 1020px;
    overflow: hidden;
    box-shadow: 0 18px 40px rgba(0, 0, 0, 0.25);
  }
  .cover-photo {
    position: absolute;
    inset: 0;
    background:
      radial-gradient(ellipse 60% 55% at 92% 78%, var(--disc-dark) 0%, var(--disc-amber) 45%, rgba(201, 141, 6, 0) 75%),
      radial-gradient(ellipse 45% 35% at 60% 48%, rgba(90, 58, 5, 0.55) 0%, rgba(90, 58, 5, 0) 70%),
      linear-gradient(160deg, var(--petal-light) 0%, var(--petal-mid) 45%, var(--petal-deep) 100%);
  }
  .spine-edge {
    position: absolute;
    top: 0; bottom: 0; left: 0;
    width: 22px;
    background: linear-gradient(90deg, var(--spine-shade), rgba(0,0,0,0));
  }
  .title-block {
    position: absolute;
    top: 110px;
    left: 70px;
    right: 40px;
    text-align: center;
    font-family: "Cinzel", serif;
    color: var(--ink-white);
    text-shadow: 2px 3px 4px rgba(0, 0, 0, 0.45);
  }
  .title-lead {
    font-size: 44px;
    font-weight: 400;
    letter-spacing: 0.5px;
    line-height: 1.05;
  }
  .title-link {
    font-size: 22px;
    color: var(--ink-gold);
    letter-spacing: 5px;
    text-shadow: none;
    margin-top: 4px;
  }
  .title-main {
    font-size: 104px;
    font-weight: 400;
    line-height: 1;
    margin-top: 2px;
    letter-spacing: 2px;
  }
  .tagline {
    position: absolute;
    top: 420px;
    left: 84px;
    width: 260px;
    font-family: "Oswald", sans-serif;
    font-weight: 500;
    font-size: 25px;
    line-height: 1.3;
    text-transform: uppercase;
    color: var(--ink-white);
    text-shadow: 1px 1px 2px rgba(0, 0, 0, 0.3);
  }
  .authors {
    position: absolute;
    bottom: 80px;
    left: 60px;
    right: 40px;
    text-align: center;
    font-family: "Cinzel", serif;
    font-size: 46px;
    line-height: 1.15;
    color: var(--ink-white);
    text-shadow: 2px 3px 4px rgba(0, 0, 0, 0.5);
  }
</style>
</head>
<body>
  <main class="canvas">
    <article class="book-cover">
      <div class="cover-photo" role="img" aria-label="Close-up photograph of a honeybee gathering pollen on a bright yellow sunflower, its dark honeycomb-like seed disc filling the lower right"></div>
      <div class="spine-edge"></div>

      <h1 class="title-block">
        <span class="title-lead">Lessons Taught</span><br>
        <span class="title-link">by the Old Orchard</span><br>
        <span class="title-main">Hives</span>
      </h1>

      <p class="tagline">A pocket guide to careful spending and caring for nature.</p>

      <p class="authors">
        Walter P. Kolb Ph. D.<br>
        Ruth P. Kolb
      </p>
    </article>
  </main>
</body>
</html>
```